Brisk Cloths, wipes multipack branding 3 types in 1 family

Brisk Cloths is a wipe producing company. For some information see our (not completed) website at briskcloths-example.nl. We also have a product named Palmbreeze (see Palmbreeze-example.com).
Our philosophy is to produce environmental friendly wipes only. We are doing that by using both bamboo and 100% bioviscose as Nonwoven. Both are biodegradable and compostable. We produce single packed wipes and multipacks (think about hygiene for hand, deodorant wipes and playtime wipes (for cleaning sex toys)). We are looking for designs for our multipacks (6 to 10 pieces per package). The size of the unfolded package foil is about 150 x 190mm (width x height) (but varies depending on the material and the number of wipes).
The branding should be modern, fresh and in line with our thoughts.

We want to have 3 packages designed for:
- Clean2Palms multipack 6 pieces
- Deodorant wipes multipack 6 pieces
- Playtime wipes multipack 10 pieces
All should have the look and feel of our Brisk Cloths logo / branding, and belong to the same family of products (to be recognised they belong together).

I added our logo as well as some examples of other packages we have been creating as samples. At first we have been thinking about using that design for multipacks as well, but we were not that happy about that.
Please consider them as a style that we liked.

Target Market(s)

Consumers
- Festival people (Clean2Palms and Deodorant)
- Adults with children (Clean2Palms)
- Travelers (Clean2Palm and Deodorant)
- Business people (Deodorant)
- Erotic industry (Playtime wipes)

Font styles to use
Sans Serif

Colors

Designer to choose colors to be used in the design.

Requirements
Must have
• A family in branding, recognisability as being part of 1 family of products.
• Branded with our logo (as attached).
• Necessary and mandatory information on the back of the package.
Nice to have
• Designs that fit to the purpose of the wipes.
• Different Colors for the different products.
• Chosen font is just because it is modern. Could be any other modern font as well.
Should not have
• Old fashioned style.
• Too much focus on the "green-ness" of the products.

```html
<!DOCTYPE html>
<html lang="en">
<head>
<meta charset="utf-8">
<title>Clean2Palms Wipe – Multipack Foil Layout</title>
<link href="https://fonts.googleapis.com/css2?family=Montserrat:wght@400;600;700;800&display=swap" rel="stylesheet">
<style>
  :root {
    --teal-base: #48a3aa;
    --teal-deep: #2f959e;
    --teal-light: #7cc3c9;
    --teal-pale: #8dd2d8;
    --ink-teal: #0b6d76;
    --white: #ffffff;
    --dimension: #1f6aa5;
    --silver-dark: #7d868c;
    --silver-mid: #a9b1b6;
    --silver-light: #dfe5e8;
  }
  html, body {
    margin: 0;
    padding: 0;
    overflow: hidden;
    background: var(--white);
  }
  .canvas {
    width: 1200px;
    height: 1200px;
    overflow: hidden;
    background: var(--white);
    font-family: "Montserrat", sans-serif;
  }
  .canvas svg { display: block; }
  .dim-line { stroke: var(--dimension); stroke-width: 1.2; fill: none; }
  .dim-arrow { fill: var(--dimension); }
  .dim-label { fill: var(--dimension); font-family: "Arial", "Helvetica", sans-serif; font-size: 24px; }
  .bg-base { fill: var(--teal-base); }
  .panel-deep { fill: var(--teal-deep); }
  .panel-light { fill: var(--teal-light); }
  .panel-pale { fill: var(--teal-pale); }
  .silver-curve { fill: none; stroke: url(#silver); stroke-width: 7; }
  .copy-title { fill: var(--white); font-weight: 600; font-size: 17px; }
  .copy-body { fill: var(--white); font-weight: 400; font-size: 14.5px; }
  .brand-name { fill: var(--white); font-weight: 600; font-size: 30px; letter-spacing: 0.5px; }
  .product-name { fill: var(--ink-teal); font-weight: 800; font-size: 44px; }
  .product-sub { fill: var(--ink-teal); font-weight: 600; font-size: 30px; letter-spacing: 22px; }
  .claim { fill: var(--ink-teal); font-weight: 600; font-size: 17px; }
  .badge { fill: var(--white); }
  .art-placeholder { fill: url(#art-tone); }
  .code-window { fill: var(--white); }
</style>
</head>
<body>
<div class="canvas">
<svg width="1200" height="1200" viewBox="0 0 1500 1500" xmlns="http://www.w3.org/2000/svg">
  <defs>
    <linearGradient id="silver" x1="0" y1="0" x2="1" y2="0">
      <stop offset="0" stop-color="var(--silver-dark)"/>
      <stop offset="0.25" stop-color="var(--silver-light)"/>
      <stop offset="0.5" stop-color="var(--silver-dark)"/>
      <stop offset="0.75" stop-color="var(--silver-light)"/>
      <stop offset="1" stop-color="var(--silver-mid)"/>
    </linearGradient>
    <linearGradient id="art-tone" x1="0" y1="0" x2="1" y2="1">
      <stop offset="0" stop-color="#8dd2d8" stop-opacity="0.35"/>
      <stop offset="1" stop-color="#8dd2d8" stop-opacity="0.6"/>
    </linearGradient>
  </defs>

  <g class="dimensions">
    <line class="dim-line" x1="336" y1="60" x2="336" y2="235"/>
    <line class="dim-line" x1="1162" y1="60" x2="1162" y2="235"/>
    <line class="dim-line" x1="306" y1="118" x2="306" y2="189"/>
    <line class="dim-line" x1="1192" y1="118" x2="1192" y2="189"/>
    <line class="dim-line" x1="380" y1="76" x2="683" y2="76"/>
    <line class="dim-line" x1="820" y1="76" x2="1118" y2="76"/>
    <polygon class="dim-arrow" points="336,76 380,65 380,87"/>
    <polygon class="dim-arrow" points="1162,76 1118,65 1118,87"/>
    <text class="dim-label" x="751" y="85" text-anchor="middle">140.00 mm</text>
    <line class="dim-line" x1="350" y1="133" x2="683" y2="133"/>
    <line class="dim-line" x1="820" y1="133" x2="1148" y2="133"/>
    <polygon class="dim-arrow" points="306,133 350,122 350,144"/>
    <polygon class="dim-arrow" points="1192,133 1148,122 1148,144"/>
    <text class="dim-label" x="751" y="142" text-anchor="middle">150.00 mm</text>

    <line class="dim-line" x1="1208" y1="189" x2="1254" y2="189"/>
    <line class="dim-line" x1="1208" y1="1310" x2="1254" y2="1310"/>
    <line class="dim-line" x1="1180" y1="248" x2="1334" y2="248"/>
    <line class="dim-line" x1="1180" y1="1251" x2="1334" y2="1251"/>
    <line class="dim-line" x1="1240" y1="232" x2="1240" y2="675"/>
    <line class="dim-line" x1="1240" y1="820" x2="1240" y2="1267"/>
    <polygon class="dim-arrow" points="1240,189 1229,232 1251,232"/>
    <polygon class="dim-arrow" points="1240,1310 1229,1267 1251,1267"/>
    <text class="dim-label" transform="translate(1249 748) rotate(-90)" text-anchor="middle">189.99 mm</text>
    <line class="dim-line" x1="1320" y1="292" x2="1320" y2="675"/>
    <line class="dim-line" x1="1320" y1="820" x2="1320" y2="1207"/>
    <polygon class="dim-arrow" points="1320,248 1309,292 1331,292"/>
    <polygon class="dim-arrow" points="1320,1251 1309,1207 1331,1207"/>
    <text class="dim-label" transform="translate(1329 748) rotate(-90)" text-anchor="middle">170.00 mm</text>
  </g>

  <g class="foil">
    <rect class="bg-base" x="306" y="189" width="886" height="1121"/>
    <path class="panel-deep" d="M497 248 L760 248 C900 350 1100 380 1162 514 L572 514 C540 440 505 330 497 248 Z"/>
    <path class="panel-light" d="M572 514 L1162 514 L1162 600 C1120 720 1050 760 960 780 C800 760 640 680 572 514 Z"/>
    <path class="panel-pale" d="M1162 600 L1162 800 C1150 870 1060 930 1040 1020 C1010 1120 1040 1200 1090 1251 L1000 1251 C900 1170 840 1080 833 920 L833 900 C840 820 900 790 960 780 C1060 760 1140 700 1162 600 Z"/>
    <path class="silver-curve" d="M572 514 C640 680 800 760 960 780"/>
    <path class="silver-curve" d="M1162 600 C1140 700 1060 760 960 780 C900 790 840 820 833 900 L833 920"/>
    <rect x="306" y="903" width="886" height="17" fill="url(#silver)"/>

    <rect class="art-placeholder" x="674" y="196" width="152" height="104" rx="6" role="img" aria-label="Illustration of a folded wet wipe"/>
    <rect class="art-placeholder" x="674" y="1198" width="152" height="104" rx="6" role="img" aria-label="Illustration of a folded wet wipe"/>

    <text class="copy-title" x="425" y="334">Comfortable wipe</text>
    <text class="copy-body">
      <tspan x="425" y="355">Wet wipe for cleaning hands and body with antibacterial effectiveness. Soft,</tspan>
      <tspan x="425" y="378">environmental and skin friendly, alcohol free, premium wipe with a natural fragrance.</tspan>
      <tspan x="425" y="418">Widely used in cars, at home, in restaurants, in beach bars, on the beach, on campsites,</tspan>
      <tspan x="425" y="441">during and after golf and in airplanes. Customers love the softness and are creative how</tspan>
      <tspan x="425" y="464">to use them.</tspan>
      <tspan x="425" y="484">Be careful, you’ll get addicted.</tspan>
    </text>

    <circle class="badge" cx="996" cy="484" r="15"/>
    <circle class="badge" cx="1061" cy="484" r="16"/>
    <circle class="badge" cx="1100" cy="484" r="14"/>

    <circle class="badge" cx="420" cy="626" r="18"/>
    <text class="brand-name" x="455" y="621">BRISK</text>
    <text class="brand-name" x="455" y="651">CLOTHS</text>

    <text class="product-name" x="928" y="616" text-anchor="middle">CLEAN2PALMS</text>
    <text class="product-sub" x="940" y="650" text-anchor="middle">WIPE</text>

    <circle class="badge" cx="413" cy="857" r="18"/>
    <circle class="badge" cx="489" cy="857" r="18"/>
    <circle class="badge" cx="565" cy="857" r="18"/>

    <text class="claim" text-anchor="middle">
      <tspan x="993" y="849">With Antibacterial</tspan>
      <tspan x="993" y="868">Effectiveness</tspan>
      <tspan x="993" y="887">Biodegradable</tspan>
    </text>

    <text class="copy-body" x="425" y="1087">Best used before the end of:</text>
    <rect class="code-window" x="336" y="1175" width="29" height="75"/>
  </g>
</svg>
</div>
</body>
</html>
```